Redesign for Popular UK Town Website

We're looking for someone to redesign a website for a popular tourist town that's visited by over 250,000 people a year. We have a basic design frame in place and need someone to make it look more 'professional.'
We've created a temporary design layout to show you a general idea of what we're looking for: http://dorrin.co.uk/
All text/images are placeholder images so you can get an idea of the general layout.
(Please note that you can grab any images found on the internet for 'tenby' to be used as placeholder images. This is because we will be visiting the locations and taking our own photos, after the design is complete.)
Target Market(s)
Tourists
Industry/Entity Type
Town
Number of Pages Required
2 page
Requirements
Must have
- You need to redesign the homepage: http://dorrin.co.uk/
- You also need to redesign the following page: http://dorrin.co.uk/hotels/ (This page will be used for multiple categories and is used to list locations of properties/places etc.)
- Design must be responsive also.
Nice to have
- Please feel free to add as much as you can to the content/features as with our limited knowledge of websites, have only been able to create a basic layout.

```html
<!DOCTYPE html>
<html lang="en">
<head>
<meta charset="utf-8">
<title>Dorrin – Welcome</title>
<link href="https://fonts.googleapis.com/css2?family=Roboto:wght@300;400;500;700&display=swap" rel="stylesheet">
<style>
:root{
  --navy:#0d3b5e;
  --navy-deep:#0a2d48;
  --accent:#1ea5e3;
  --ink:#222;
  --muted:#6a6a6a;
  --line:#e6e6e6;
  --paper:#fff;
  --pale:#f1f2f3;
  --footer:#2b2b2b;
  --footer-text:#cfcfcf;
}
*{box-sizing:border-box;margin:0;padding:0}
html,body{width:1200px;height:2769px;overflow:hidden}
body{font-family:"Roboto",Arial,sans-serif;color:var(--ink);background:var(--paper);position:relative}
a{color:inherit;text-decoration:none}

/* header */
.site-header{position:absolute;top:0;left:0;width:1200px;height:103px;background:var(--paper);display:flex;align-items:center;padding:0 74px}
.brand{display:flex;align-items:center;gap:10px}
.brand-mark{width:38px;height:38px;border-radius:50%;background:var(--navy)}
.brand-name{font-size:27px;font-weight:700;color:var(--navy);letter-spacing:-.5px}
.main-nav{display:flex;gap:30px;margin-left:auto;margin-right:46px;font-size:16px;font-weight:500;color:#1d1d1d}
.btn-contact{width:136px;height:41px;border-radius:21px;background:var(--navy);color:#fff;font-size:15px;font-weight:500;display:flex;align-items:center;justify-content:center}

/* hero */
.hero{position:absolute;top:103px;left:0;width:1200px;height:552px;background:linear-gradient(180deg,#1d4a6e 0%,#0f3a5c 55%,#0c3352 100%);text-align:center;color:#fff}
.hero-emblem{width:82px;height:82px;margin:80px auto 0;border-radius:50%;border:4px solid #fff}
.hero-title{display:flex;align-items:center;justify-content:center;gap:16px;margin-top:24px;font-size:36px;font-weight:500;letter-spacing:.5px}
.hero-title span{color:var(--accent)}
.hero-title .flag{width:40px;height:22px;background:#fff;clip-path:polygon(0 0,100% 0,100% 100%,0 100%,22% 50%)}
.hero-title .flag.right{clip-path:polygon(0 0,100% 0,78% 50%,100% 100%,0 100%)}
.hero-intro{width:780px;margin:22px auto 0;font-size:16px;font-weight:300;line-height:26px}

.band{position:absolute;top:655px;left:0;width:1200px;height:235px;background:var(--pale)}

.highlights{position:absolute;top:545px;left:74px;display:flex;gap:28px}
.highlight-card{width:332px;height:290px;background:#fff;border-radius:8px;padding:9px 9px 0;box-shadow:0 2px 8px rgba(0,0,0,.12);text-align:center}
.highlight-photo{height:222px;border-radius:8px}
.highlight-card h3{font-size:16px;font-weight:400;margin-top:22px}

/* listings */
.listings{position:absolute;top:947px;left:74px;width:692px}
.listing{display:flex;gap:28px;height:295px;position:relative}
.listing+.listing::before{content:"";position:absolute;top:-27px;left:360px;right:0;height:1px;background:var(--line)}
.listing-photo{width:332px;height:240px;flex:none}
.listing-body{width:332px}
.listing-title{font-size:22px;font-weight:500;line-height:26px;margin-top:-2px}
.listing-text{font-size:12.5px;line-height:22px;color:#555;margin-top:14px}
.listing-actions{display:flex;margin-top:29px;border:1px solid var(--line);height:96px}
.action{flex:1;display:flex;flex-direction:column;align-items:center;justify-content:center;gap:12px;font-size:13px;color:#555}
.action+.action{border-left:1px solid var(--line)}
.action svg{width:24px;height:24px;stroke:#9a9a9a;fill:none;stroke-width:1.5}

.load-more{position:absolute;top:2440px;left:360px;display:flex;align-items:center;gap:12px;font-size:14px;font-weight:500}
.load-more .dot{width:34px;height:34px;border-radius:50%;border:3px solid var(--navy)}

/* sidebar */
.sidebar{position:absolute;top:947px;left:849px;width:277px}
.promo{height:552px;background:linear-gradient(180deg,#6f8496 0%,#8a9aa3 35%,#6e8a4a 70%,#557a3a 100%);position:relative;color:#fff;padding:18px 24px}
.promo h4{font-size:27px;font-weight:500;line-height:33px;max-width:200px}
.promo .book{display:inline-block;margin-top:14px;background:#e8414f;font-size:10px;padding:6px 20px}
.promo .promo-brand{position:absolute;left:0;right:0;bottom:26px;text-align:center;font-size:22px;font-weight:500}
.promo .promo-brand small{display:block;font-size:11px;font-weight:400;margin-top:4px}
.feed-heading{margin-top:40px;font-size:20px;font-weight:500;color:var(--accent)}
.feed{margin-top:14px;height:511px;border:1px solid #ddd;font-size:11px;color:#333}
.feed-head{padding:12px 10px;font-size:17px;border-bottom:1px solid #e5e5e5}
.feed-head small{font-size:10px;color:var(--muted)}
.tweet{padding:10px 14px;border-bottom:1px solid #e5e5e5}
.tweet-user{display:flex;gap:10px;align-items:center;margin-bottom:8px}
.avatar{width:28px;height:28px;border-radius:50%;background:#c9d6df;flex:none}
.tweet-user b{display:block;font-size:11px}
.tweet-user i{font-style:normal;color:var(--muted);font-size:10px}
.tweet .tag{color:var(--accent)}
.tweet-photo{height:160px;margin-top:10px;background:linear-gradient(180deg,#9cc7e2 0%,#3e9fc4 45%,#d9b982 75%,#c79c5e 100%)}
.retweet{font-size:10px;color:#4caf50;margin-bottom:6px}
.feed-foot{display:flex;justify-content:space-between;padding:8px 10px;font-size:10px;color:var(--accent)}

/* footer */
.site-footer{position:absolute;top:2548px;left:0;width:1200px;height:221px;background:var(--footer);color:var(--footer-text)}
.footer-col{position:absolute;top:44px}
.footer-col h5{font-size:15.5px;font-weight:500;color:#fff;margin-bottom:14px}
.newsletter{left:74px}
.newsletter .field{width:242px;height:40px;border-radius:20px;background:#fff;color:#999;font-size:13px;padding:0 24px;display:flex;align-items:center}
.newsletter .subscribe{margin-top:14px;width:120px;height:40px;border-radius:20px;background:var(--accent);color:#fff;font-size:13px;font-weight:500;display:flex;align-items:center;justify-content:center}
.quick-links{left:406px}
.quick-links li{list-style:none;font-size:13.5px;line-height:22px}
.social{left:677px}
.social-icons{display:flex;gap:12px}
.social-icons span{width:38px;height:38px;border-radius:50%;background:#555}
.footer-mark{position:absolute;left:958px;top:40px;width:96px;height:96px;border-radius:50%;border:5px solid #6a6a6a}
.copyright{position:absolute;left:940px;top:169px;font-size:13px}
</style>
</head>
<body>

<header class="site-header">
  <a class="brand" href="#"><span class="brand-mark"></span><span class="brand-name">SeaHelm</span></a>
  <nav class="main-nav">
    <a href="#">Where to Stay</a>
    <a href="#">Caravan and Camping</a>
    <a href="#">Bed and Breakfast</a>
    <a href="#">Hotels in Dorrin</a>
  </nav>
  <a class="btn-contact" href="#">Contact Us</a>
</header>

<section class="hero" role="img" aria-label="Dusk view over the rooftops of the old town in deep blue tones">
  <div class="hero-emblem"></div>
  <h1 class="hero-title"><i class="flag"></i>WELCOME TO <span>DORRIN</span><i class="flag right"></i></h1>
  <p class="hero-intro">The jewel in the crown of Pembrokeshire. A popular harbour town visited by over 299,000 visitors a year. Surrounded by its medieval stone wall, Dorrin is steeped with history and beautiful landscapes. Famed for it's beautiful beaches and views that will lure you to come back each year, we hope you enjoy your time visting and breathing in the sea air of Dorrin.</p>
</section>

<div class="band"></div>

<section class="highlights">
  <article class="highlight-card">
    <div class="highlight-photo" role="img" aria-label="Riverside town with a stone bridge and green trees" style="background:linear-gradient(180deg,#8a8f9e 0%,#b59a6a 40%,#5e8a3c 75%,#3f6b2a 100%)"></div>
    <h3>Things To Do</h3>
  </article>
  <article class="highlight-card">
    <div class="highlight-photo" role="img" aria-label="Harbour with colourful houses and boats below a wooded headland" style="background:linear-gradient(180deg,#9fb6c9 0%,#5f7f46 35%,#c9a6a0 55%,#4d7a8c 80%,#3d6a4a 100%)"></div>
    <h3>Place To Eat</h3>
  </article>
  <article class="highlight-card">
    <div class="highlight-photo" role="img" aria-label="Cobbled old town square at sunset" style="background:linear-gradient(180deg,#3d6aa8 0%,#e9a050 40%,#b89a7a 65%,#7a6a5e 100%)"></div>
    <h3>Where To Stay</h3>
  </article>
</section>

<main class="listings">
  <article class="listing">
    <div class="listing-photo" role="img" aria-label="Pale green hotel frontage with flags" style="background:linear-gradient(180deg,#c9d9d6 0%,#a9c3bd 60%,#7b8b86 100%)"></div>
    <div class="listing-body">
      <h2 class="listing-title">Fernridge Hotel</h2>
      <p class="listing-text">With tourist flocking to Dorrin every year, there's never a shortage of things to do. This is our top 10 things to do in Dorrin and the surrounding area.</p>
      <div class="listing-actions">
        <a class="action" href="#"><svg viewBox="0 0 24 24"><path d="M6 3l3 4-2 2a12 12 0 0 0 8 8l2-2 4 3-2 3C10 21 3 14 3 5z"/></svg>Call Us</a>
        <a class="action" href="#"><svg viewBox="0 0 24 24"><rect x="3" y="6" width="18" height="12"/><path d="M3 6l9 7 9-7"/></svg>Email Us</a>
        <a class="action" href="#"><svg viewBox="0 0 24 24"><path d="M18 13v7H4V6h7M14 4h6v6M20 4l-9 9"/></svg>Website</a>
      </div>
    </div>
  </article>
  <article class="listing">
    <div class="listing-photo" role="img" aria-label="White hotel entrance with columns and a tree" style="background:linear-gradient(180deg,#7fb0e0 0%,#e9ecef 35%,#d5d2c8 70%,#6a6a60 100%)"></div>
    <div class="listing-body">
      <h2 class="listing-title">The Lawnside Hotel</h2>
      <p class="listing-text">With tourist flocking to Dorrin every year, there's never a shortage of things to do. This is our top 10 things to do in Dorrin and the surrounding area.</p>
      <div class="listing-actions">
        <a class="action" href="#"><svg viewBox="0 0 24 24"><path d="M6 3l3 4-2 2a12 12 0 0 0 8 8l2-2 4 3-2 3C10 21 3 14 3 5z"/></svg>Call Us</a>
        <a class="action" href="#"><svg viewBox="0 0 24 24"><rect x="3" y="6" width="18" height="12"/><path d="M3 6l9 7 9-7"/></svg>Email Us</a>
        <a class="action" href="#"><svg viewBox="0 0 24 24"><path d="M18 13v7H4V6h7M14 4h6v6M20 4l-9 9"/></svg>Website</a>
      </div>
    </div>
  </article>
  <article class="listing">
    <div class="listing-photo" role="img" aria-label="Tall white terraced hotel with balconies" style="background:linear-gradient(180deg,#e6e8ea 0%,#d9d9d6 60%,#5c5c5c 100%)"></div>
    <div class="listing-body">
      <h2 class="listing-title">The Cliffe Marlow Hotel</h2>
      <p class="listing-text">With tourist flocking to Dorrin every year, there's never a shortage of things to do. This is our top 10 things to do in Dorrin and the surrounding area.</p>
      <div class="listing-actions">
        <a class="action" href="#"><svg viewBox="0 0 24 24"><path d="M6 3l3 4-2 2a12 12 0 0 0 8 8l2-2 4 3-2 3C10 21 3 14 3 5z"/></svg>Call Us</a>
        <a class="action" href="#"><svg viewBox="0 0 24 24"><rect x="3" y="6" width="18" height="12"/><path d="M3 6l9 7 9-7"/></svg>Email Us</a>
        <a class="action" href="#"><svg viewBox="0 0 24 24"><path d="M18 13v7H4V6h7M14 4h6v6M20 4l-9 9"/></svg>Website</a>
      </div>
    </div>
  </article>
  <article class="listing">
    <div class="listing-photo" role="img" aria-label="Cream hotel terrace with green balcony railings" style="background:linear-gradient(180deg,#eceee9 0%,#d6d8cf 50%,#6f8a5a 80%,#4a4a40 100%)"></div>
    <div class="listing-body">
      <h2 class="listing-title">Calder House Hotel</h2>
      <p class="listing-text">With tourist flocking to Dorrin every year, there's never a shortage of things to do. This is our top 10 things to do in Dorrin and the surrounding area.</p>
      <div class="listing-actions">
        <a class="action" href="#"><svg viewBox="0 0 24 24"><path d="M6 3l3 4-2 2a12 12 0 0 0 8 8l2-2 4 3-2 3C10 21 3 14 3 5z"/></svg>Call Us</a>
        <a class="action" href="#"><svg viewBox="0 0 24 24"><rect x="3" y="6" width="18" height="12"/><path d="M3 6l9 7 9-7"/></svg>Email Us</a>
        <a class="action" href="#"><svg viewBox="0 0 24 24"><path d="M18 13v7H4V6h7M14 4h6v6M20 4l-9 9"/></svg>Website</a>
      </div>
    </div>
  </article>
  <article class="listing">
    <div class="listing-photo" role="img" aria-label="White corner hotel under a blue sky" style="background:linear-gradient(180deg,#4f8fd6 0%,#a7c6ea 35%,#efefef 60%,#5a5a55 100%)"></div>
    <div class="listing-body">
      <h2 class="listing-title">The Alderney Hotel</h2>
      <p class="listing-text">With tourist flocking to Dorrin every year, there's never a shortage of things to do. This is our top 10 things to do in Dorrin and the surrounding area.</p>
      <div class="listing-actions">
        <a class="action" href="#"><svg viewBox="0 0 24 24"><path d="M6 3l3 4-2 2a12 12 0 0 0 8 8l2-2 4 3-2 3C10 21 3 14 3 5z"/></svg>Call Us</a>
        <a class="action" href="#"><svg viewBox="0 0 24 24"><rect x="3" y="6" width="18" height="12"/><path d="M3 6l9 7 9-7"/></svg>Email Us</a>
        <a class="action" href="#"><svg viewBox="0 0 24 24"><path d="M18 13v7H4V6h7M14 4h6v6M20 4l-9 9"/></svg>Website</a>
      </div>
    </div>
  </article>
</main>

<a class="load-more" href="#"><span class="dot"></span>Load more</a>

<aside class="sidebar">
  <div class="promo" role="img" aria-label="Advert showing a glass pyramid house on a green hillside by the sea">
    <h4>Book a view with a room.</h4>
    <span class="book">Book Now ›</span>
    <div class="promo-brand">Stayloft<small>Stay Anywhere</small></div>
  </div>
  <h3 class="feed-heading">Live Feed</h3>
  <div class="feed">
    <div class="feed-head">Tweets <small>by @DorrinOfficial</small></div>
    <div class="tweet">
      <div class="tweet-user"><span class="avatar"></span><div><b>Visit Dorrin Official</b><i>@DorrinOfficial</i></div></div>
      <p>And we look forward to welcoming Tamsin back</p>
    </div>
    <div class="tweet">
      <p class="retweet">Visit Dorrin Official Retweeted</p>
      <div class="tweet-user"><span class="avatar"></span><div><b>Roam With Jo</b><i>@RoamWithJo</i></div></div>
      <p>The coastline here is stunning <span class="tag">@DorrinOfficial @visitcoast #SeeTheShore</span></p>
      <div class="tweet-photo" role="img" aria-label="Sandy beach and island seen from the cliffs"></div>
    </div>
    <div class="tweet"><p class="retweet">Visit Dorrin Official Retweeted</p></div>
    <div class="feed-foot"><span>Embed</span><span>View on feed</span></div>
  </div>
</aside>

<footer class="site-footer">
  <div class="footer-col newsletter">
    <h5>Newsletter Sign Up</h5>
    <div class="field">Email Address</div>
    <a class="subscribe" href="#">SUBSCRIBE</a>
  </div>
  <div class="footer-col quick-links">
    <h5>Quick Links</h5>
    <ul>
      <li>Where to Stay</li>
      <li>Caravan and Camping</li>
      <li>Bed and Breakfast</li>
      <li>Hotels in Dorrin</li>
    </ul>
  </div>
  <div class="footer-col social">
    <h5>We're Social</h5>
    <div class="social-icons"><span></span><span></span><span></span></div>
  </div>
  <div class="footer-mark"></div>
  <p class="copyright">©2017 Dorrin.co.uk</p>
</footer>

</body>
</html>
```